Corvella Group Tank Card. New Design

We need a new design for our Credit Card Tank. We want a modern design using our logo colors. Our Card measures are 8,5cmX5,5cm. You can upgrade our logo design too. We are looking for modern and cool design. Our card printers can print the card number and holder in white color then you can use the colors you want for the background.

Target Market(s)

Gas station customers

Industry/Entity Type

Credit Card

Font styles to use
Sans Serif

Colors
a54499
b768aa
d2a4cc
acd036
cadf82
9bcb3b

Requirements
Must have
• Cool Design

```html
<!DOCTYPE html>
<html lang="en">
<head>
<meta charset="utf-8">
<title>Corvella Group Tank Card</title>
<link rel="stylesheet" href="https://fonts.googleapis.com/css2?family=Oswald:wght@600&family=Share+Tech+Mono&family=Montserrat:wght@500;600&display=swap">
<style>
  :root {
    --bg: #ececee;
    --green: #9bcb3b;
    --green-light: #acd036;
    --green-dark: #6a8f25;
    --magenta: #c40aa6;
    --magenta-deep: #850670;
    --purple-brand: #8b0f7a;
    --ink: #111111;
    --white: #ffffff;
  }
  * { margin: 0; padding: 0; box-sizing: border-box; }
  html, body { width: 1200px; height: 1200px; overflow: hidden; }
  body { background: var(--bg); position: relative; }
  .card { position: absolute; width: 614px; height: 386px; border-radius: 18px; overflow: hidden; }
  .card svg { display: block; width: 100%; height: 100%; }
  .card--front { left: 258px; top: 180px; }
  .card--back { left: 330px; top: 640px; }
  .brand-name { font-family: "Oswald", sans-serif; font-weight: 600; fill: var(--purple-brand); }
  .card-number, .card-meta, .holder-name { font-family: "Share Tech Mono", monospace; fill: var(--white); }
  .back-label { font-family: "Montserrat", sans-serif; font-weight: 600; fill: var(--ink); }
  .back-note { font-family: "Montserrat", sans-serif; font-weight: 500; fill: var(--green-light); }
  .issuer-name { font-family: "Montserrat", sans-serif; font-weight: 500; fill: var(--green-dark); }
</style>
</head>
<body>

<div class="card card--front">
  <svg viewBox="0 0 614 386" xmlns="http://www.w3.org/2000/svg">
    <defs>
      <linearGradient id="greenSheen" x1="0" y1="0" x2="1" y2="0">
        <stop offset="0" stop-color="#6f9a27"/>
        <stop offset="0.35" stop-color="#9bcb3b"/>
        <stop offset="0.75" stop-color="#8cb832"/>
        <stop offset="1" stop-color="#5e8422"/>
      </linearGradient>
      <linearGradient id="magentaSheen" x1="0" y1="0" x2="1" y2="0">
        <stop offset="0" stop-color="#9b0a84"/>
        <stop offset="0.45" stop-color="#d60ab2"/>
        <stop offset="1" stop-color="#7a0466"/>
      </linearGradient>
      <linearGradient id="chipGold" x1="0" y1="0" x2="1" y2="1">
        <stop offset="0" stop-color="#b48a1c"/>
        <stop offset="0.5" stop-color="#e6e0a8"/>
        <stop offset="1" stop-color="#b99124"/>
      </linearGradient>
    </defs>
    <rect class="card-base" width="614" height="386" fill="url(#greenSheen)"/>
    <path class="swoosh" d="M0,296 C250,296 480,200 602,0 L614,0 L614,386 L0,386 Z" fill="url(#magentaSheen)"/>
    <path class="swoosh-shade" d="M0,386 C300,340 520,250 614,40 L614,386 Z" fill="#7a0466" opacity="0.55"/>

    <rect class="pump-area" role="img" aria-label="Fuel pump silhouette" x="378" y="38" width="170" height="272" rx="10" fill="#2a3a10" opacity="0.28"/>

    <text class="brand-name" x="62" y="88" font-size="50">CORVELLA GROUP</text>

    <rect class="chip" role="img" aria-label="Payment chip" x="62" y="106" width="97" height="80" rx="7" fill="url(#chipGold)" stroke="#222" stroke-width="1.5"/>

    <text class="card-number" font-size="38" y="246">
      <tspan x="62">1234</tspan><tspan x="192">5678</tspan><tspan x="320">1234</tspan><tspan x="450">5678</tspan>
    </text>

    <text class="card-meta" font-size="14" letter-spacing="1.5"><tspan x="58" y="340">VALID THRU</tspan><tspan x="58" y="356">01/18</tspan></text>
    <text class="holder-name" x="336" y="354" font-size="21" letter-spacing="2">MR NAME SURNAME</text>
  </svg>
</div>

<div class="card card--back">
  <svg viewBox="0 0 614 386" xmlns="http://www.w3.org/2000/svg">
    <defs>
      <linearGradient id="backSheen" x1="0" y1="0" x2="1" y2="1">
        <stop offset="0" stop-color="#a3088a"/>
        <stop offset="0.35" stop-color="#d10cb0"/>
        <stop offset="0.7" stop-color="#9c0884"/>
        <stop offset="1" stop-color="#7d0568"/>
      </linearGradient>
      <linearGradient id="silverPanel" x1="0" y1="0" x2="1" y2="0">
        <stop offset="0" stop-color="#c9c9c9"/>
        <stop offset="0.3" stop-color="#f2f2f2"/>
        <stop offset="0.6" stop-color="#b4b4b4"/>
        <stop offset="0.85" stop-color="#efefef"/>
        <stop offset="1" stop-color="#a8a8a8"/>
      </linearGradient>
    </defs>
    <rect class="card-base" width="614" height="386" fill="url(#backSheen)"/>
    <path class="back-swoosh" d="M380,120 C470,150 560,170 614,200 L614,240 C540,210 460,190 380,120 Z" fill="#ffffff" opacity="0.08"/>
    <path class="back-swoosh" d="M420,200 C480,250 540,290 614,300 L614,330 C530,320 470,280 420,200 Z" fill="#ffffff" opacity="0.07"/>
    <path class="back-swoosh" d="M250,280 C380,300 520,280 614,250 L614,386 L250,386 Z" fill="#6e0459" opacity="0.35"/>

    <rect class="magnetic-stripe" x="0" y="48" width="614" height="78" fill="#000"/>

    <text class="back-label" x="56" y="152" font-size="14">AUTHORISED SIGNATURE</text>
    <rect class="signature-panel" x="56" y="160" width="525" height="62" fill="url(#silverPanel)"/>
    <text class="back-label" x="56" y="244" font-size="14">NOT VALID UNLESS SIGN</text>
    <text class="back-note" font-size="13"><tspan x="56" y="266">this card is property of BANK NAME</tspan><tspan x="56" y="284">If found,please return to the nearest BANK NAME</tspan></text>

    <text class="issuer-name" x="584" y="354" font-size="23" text-anchor="end">BANK NAME</text>
  </svg>
</div>

</body>
</html>
```